Hi,
We are an accounting firm looking to upgrade the following:
Logo, letterhead, withcomp slips and maybe our business cards. I have attached our original letterhead (sample A) and a letterhead (SAmple B) which we like the design and layout, however I want to stick with the colours of our orginal letterhead (Sample A) but improve and modernise the look with other letter head (Sample B) I have attached both. On the footer of Sample A, we would like to remove the names of the directors but leave EST. 1985 we also want to add the QRT logo ABN and TAX AGENT logo as stated in Sample B , we would like to do a layout for the header similar to SAmple B however maybe a bit more structured.

```html
<!DOCTYPE html>
<html lang="en">
<head>
<meta charset="utf-8">
<title>Brentholm Accountants – Letterhead</title>
<link href="https://fonts.googleapis.com/css2?family=Quicksand:wght@500;600;700&display=swap" rel="stylesheet">
<style>
  :root {
    --backdrop: #b4b4b4;
    --paper: #f0f0f0;
    --navy: #3d5a83;
    --ink: #4f4f4f;
    --sign: #9a8470;
    --badge-red: #d9434b;
    --badge-blue: #3aa3d8;
    --badge-green: #9cc63b;
  }
  * { margin: 0; padding: 0; box-sizing: border-box; }
  html, body { width: 1200px; height: 900px; overflow: hidden; }
  body {
    background: var(--backdrop);
    font-family: "Quicksand", sans-serif;
    color: var(--ink);
    position: relative;
  }
  .letterhead {
    position: absolute;
    left: 303px; top: 30px;
    width: 594px; height: 840px;
    background: var(--paper);
  }
  .brand {
    position: absolute; left: 52px; top: 60px;
    display: flex; align-items: center; gap: 7px;
  }
  .brand-square { width: 12px; height: 12px; background: var(--navy); }
  .brand-name {
    font-weight: 700; font-size: 27px; color: var(--navy);
    letter-spacing: -0.5px; line-height: 1;
  }
  .contact-row {
    position: absolute; right: 52px;
    display: flex; align-items: center; gap: 8px;
    font-size: 6.2px; font-weight: 600; color: var(--navy);
    white-space: nowrap;
  }
  .contact-row svg { width: 15px; height: 15px; flex: none; }
  .contact-row .spacer { width: 4px; }
  .row-address { top: 61px; }
  .row-phones { top: 83px; }
  .row-web { top: 105px; }
  .date {
    position: absolute; right: 70px; top: 162px;
    font-size: 12px; font-weight: 500;
  }
  .salutation {
    position: absolute; left: 71px; top: 196px;
    font-size: 12.5px; font-weight: 500;
  }
  .body-copy {
    position: absolute; left: 73px; width: 452px;
    font-size: 11px; font-weight: 500; line-height: 19.2px;
    text-align: justify;
  }
  .para-1 { top: 238px; }
  .para-2 { top: 341px; }
  .para-3 { top: 443px; }
  .signature {
    position: absolute; left: 73px; top: 566px;
    width: 122px; height: 60px;
    background: linear-gradient(90deg, rgba(154,132,112,0.22), rgba(154,132,112,0.05));
    border-radius: 4px;
  }
  .signatory {
    position: absolute; left: 73px; top: 642px;
    font-size: 12.5px; font-weight: 500; line-height: 23px;
  }
  .footer-text {
    position: absolute; left: 53px; top: 765px;
    font-size: 6px; font-weight: 600; color: var(--navy); line-height: 9.5px;
    white-space: nowrap;
  }
  .footer-text strong { font-weight: 700; }
  .footer-text .sep { margin: 0 4px; }
  .badge {
    position: absolute; top: 750px;
  }
  .badge-membership { left: 388px; width: 36px; height: 36px; }
  .badge-registered { left: 475px; width: 36px; height: 36px; }
  .tax-agent {
    position: absolute; left: 516px; top: 761px;
    font-size: 4.6px; font-weight: 700; color: var(--navy); line-height: 6px;
  }
</style>
</head>
<body>
  <main class="letterhead">
    <div class="brand">
      <span class="brand-square"></span>
      <span class="brand-name">Brentholm</span>
    </div>

    <div class="contact-row row-address">
      <span>Brentholm Pty Ltd 48 Carrow Lane Ashvale, Victoria 3190 Australia&nbsp; ABN 41 572 309 816</span>
      <svg viewBox="0 0 20 20" aria-hidden="true"><circle cx="10" cy="10" r="10" fill="var(--navy)"/><path d="M10 4.5a3.6 3.6 0 0 0-3.6 3.6c0 2.7 3.6 6.9 3.6 6.9s3.6-4.2 3.6-6.9A3.6 3.6 0 0 0 10 4.5z" fill="#fff"/><circle cx="10" cy="8.1" r="1.4" fill="var(--navy)"/></svg>
    </div>

    <div class="contact-row row-phones">
      <span>info@brentholm.com.au</span>
      <span class="spacer"></span>
      <svg viewBox="0 0 20 20" aria-hidden="true"><circle cx="10" cy="10" r="10" fill="var(--navy)"/><rect x="5" y="6.5" width="10" height="7" rx="1" fill="none" stroke="#fff" stroke-width="1.2"/><path d="M5.3 7l4.7 3.6L14.7 7" fill="none" stroke="#fff" stroke-width="1.2"/></svg>
      <span class="spacer"></span>
      <span>61+3 9400 1287</span>
      <span class="spacer"></span>
      <svg viewBox="0 0 20 20" aria-hidden="true"><circle cx="10" cy="10" r="10" fill="var(--navy)"/><rect x="7" y="5" width="6" height="3" fill="none" stroke="#fff" stroke-width="1.1"/><rect x="5" y="8" width="10" height="5" rx="1" fill="none" stroke="#fff" stroke-width="1.1"/><rect x="7" y="11" width="6" height="4" fill="var(--navy)" stroke="#fff" stroke-width="1.1"/></svg>
      <span class="spacer"></span>
      <span>61+3 9411 3920</span>
      <svg viewBox="0 0 20 20" aria-hidden="true"><circle cx="10" cy="10" r="10" fill="var(--navy)"/><path d="M6.5 5.5l2 .2.8 2.3-1.2 1c.6 1.3 1.6 2.3 2.9 2.9l1-1.2 2.3.8.2 2c-.3.6-1 1-1.7 1-4 0-7.3-3.3-7.3-7.3 0-.7.4-1.4 1-1.7z" fill="#fff"/></svg>
    </div>

    <div class="contact-row row-web">
      <span>www.brentholmaccountants.com.au</span>
      <svg viewBox="0 0 20 20" aria-hidden="true"><circle cx="10" cy="10" r="10" fill="var(--navy)"/><g fill="none" stroke="#fff" stroke-width="1.1"><circle cx="10" cy="10" r="5"/><ellipse cx="10" cy="10" rx="2.2" ry="5"/><path d="M5 10h10M6 7.3h8M6 12.7h8"/></g></svg>
    </div>

    <p class="date">July 25, 2025</p>
    <p class="salutation">Dear Delia Frampton</p>

    <p class="body-copy para-1">Lorem ipsum dolor sit amet, consectetuer adipiscing elit, sed diam nonummy nibh euismod tincidunt ut laoreet dolore magna aliquam erat volutpat. Ut wisi enim ad minim veniam, quis nostrud exerci tation ullamcorper suscipit lobortis nisl ut aliquip ex ea commodo consequat.</p>
    <p class="body-copy para-2">Duis autem vel eum iriure dolor in hendrerit in vulputate velit esse molestie consequat, vel illum dolore eu feugiat nulla facilisis at vero eros et accumsan et iusto odio dignissim qui blandit praesent luptatum zril delenit augue duis dolore te feugait nulla facilisi.</p>
    <p class="body-copy para-3">Lorem ipsum dolor sit amet, consectetuer adipiscing elit, sed diam nonummy nibh euismod tincidunt ut laoreet dolore magna aliquam erat volutpat. Ut wisi enim ad minim veniam, quis nostrud exerci tation ullamcorper suscipit lobortis nisl ut aliquip ex ea commodo consequat.</p>

    <div class="signature" role="img" aria-label="Handwritten signature of the manager"></div>
    <p class="signatory">Rowan Ellis Tate<br>Manager</p>

    <div class="footer-text">
      <strong>EST. 1985 Certified Practising Accountants</strong><span class="sep">|</span>Norvale Advisory (MEL) Pty Limited<span class="sep">|</span>ABN 63 118 204 597<br>
      Liability limited by a scheme approved under Profesional Standards Legislation
    </div>

    <svg class="badge badge-membership" viewBox="0 0 36 36" role="img" aria-label="Professional membership badge">
      <rect x="4" y="4" width="28" height="28" rx="4" fill="var(--badge-blue)"/>
    </svg>
    <svg class="badge badge-registered" viewBox="0 0 36 36" role="img" aria-label="Registered tax agent badge">
      <circle cx="18" cy="18" r="17" fill="#e2e2e2" stroke="#9a9a9a" stroke-width="1"/>
      <circle cx="18" cy="18" r="10" fill="var(--badge-green)"/>
    </svg>
    <p class="tax-agent">TAX AGENT<br>48213706</p>
  </main>
</body>
</html>
```